Web Site Design

We need to design the whole web site for our small start up. We sell hospitality and culinary art internships abroad. I did my own design with WIX which is horrible meanwhile I started with my business. You can see it www.brightvoyage-intern.example I will need you to create a new and attractive web site and to leave it working on wix. The internship destinations are United Arab Emirates, Thailand, China, Spain, Brazil and maybe leave a couple of pages for future destinations.You could also get other ideas of other sites that do internships.

Target Market(s)

Students and recent graduates of hospitality and culinary art majors

Industry/Entity Type

Education

Number of Pages Required

5+ page

Requirements
Must have
• Addittional to our program destinations, or to the pages in the current site. The website must contain a page for Universities or Hotels who require our service

```html
<!DOCTYPE html>
<html lang="en">
<head>
<meta charset="utf-8">
<title>Bright Voyage – Hospitality Internships</title>
<link rel="stylesheet" href="https://fonts.googleapis.com/css2?family=Open+Sans:wght@400;600;700&family=Merriweather:ital,wght@0,400;1,700&display=swap">
<style>
:root{
  --navy:#1f3a63;
  --bar:#3e5f87;
  --orange:#e8935a;
  --orange-text:#e07d45;
  --field:#e9eef5;
  --grey:#5a5f66;
  --ink:#1a1a1a;
}
*{box-sizing:border-box;margin:0;padding:0}
html,body{width:900px;height:1200px;overflow:hidden;background:#fff;font-family:"Open Sans",Arial,sans-serif;color:var(--ink)}
.page{position:relative;width:900px;height:1200px}
.abs{position:absolute}
.topbar{left:0;top:0;width:900px;height:19px;background:var(--bar);color:#fff;font-size:8px}
.topbar .mail{left:162px;top:4px;display:flex;align-items:center;gap:6px}
.topbar .phone{right:120px;top:4px;display:flex;align-items:center;gap:5px}
.nav{left:0;top:19px;width:900px;height:43px;background:#fff}
.brand{left:162px;top:12px;display:flex;align-items:center;gap:6px;font-size:11px;font-weight:700;color:var(--navy)}
.brand .dot{width:18px;height:18px;border-radius:50%;background:var(--navy)}
.menu{left:314px;top:16px;display:flex;gap:22px;font-size:9.5px;letter-spacing:.2px}
.search{left:638px;top:15px;width:141px;height:17px;border:1px solid #222;font-size:8px;padding:3px 7px}
.search .btn{position:absolute;right:0;top:0;width:25px;height:15px;border-left:1px solid #222;display:flex;align-items:center;justify-content:center}
.hero{left:0;top:62px;width:900px;height:309px;background:linear-gradient(100deg,#3d5676 0%,#6f7fa4 38%,#9a88b0 58%,#d98c8a 82%,#e59b6e 100%)}
.hero h1{left:166px;top:126px;width:340px;font-family:"Merriweather",Georgia,serif;font-style:italic;font-weight:700;font-size:18px;line-height:22px;color:#fff}
.form{left:524px;top:84px;width:256px;height:289px;background:#fff;box-shadow:0 3px 8px rgba(0,0,0,.18)}
.form h2{position:absolute;left:0;top:13px;width:100%;text-align:center;font-family:"Merriweather",Georgia,serif;font-weight:400;font-size:16px;line-height:20px;color:var(--orange-text)}
.field{position:absolute;left:11px;width:235px;background:var(--field);font-size:8.5px;color:#777;padding:12px 12px}
.send{position:absolute;left:11px;top:249px;width:235px;height:32px;background:var(--orange);color:#fff;font-size:13px;text-align:center;line-height:32px}
.title{left:0;width:900px;text-align:center;font-size:15px;color:var(--navy);letter-spacing:.3px}
.about-text{left:230px;top:430px;width:440px;text-align:center;font-size:10.5px;line-height:14px;color:var(--grey)}
.outline-btn{left:412px;top:501px;width:78px;height:20px;border:1px solid var(--navy);border-radius:4px;font-size:8px;text-align:center;line-height:18px;color:var(--navy)}
.divider{left:100px;top:556px;width:700px;height:12px;background:radial-gradient(ellipse at center top,rgba(0,0,0,.14),rgba(0,0,0,0) 70%)}
.tabs{left:0;top:620px;width:900px;display:flex;justify-content:center;gap:26px;font-size:11px;color:var(--navy)}
.tabs .on{border-bottom:1px solid var(--orange);padding-bottom:3px}
.photo{display:flex;flex-direction:column;align-items:center;justify-content:center;color:#fff}
.dest{top:655px;width:155px;height:124px}
.dest .name{font-weight:700;font-size:14px;margin-bottom:6px}
.pill{background:#fff;color:#444;font-size:8px;border-radius:4px;padding:4px 21px}
.unis{left:0;top:807px;width:900px;height:232px;background:linear-gradient(180deg,#2b4a78,#1f3658 60%,#25314a)}
.uni{top:877px;width:149px;height:105px;border:1px solid #fff}
.uni .name{font-weight:700;font-size:12.5px;line-height:17px;text-align:center}
.white-btn{left:418px;top:1002px;width:78px;height:20px;background:#fff;border-radius:3px;font-size:8px;text-align:center;line-height:20px;color:#222}
.foot-about{left:131px;top:1070px;width:190px;font-size:7.8px;line-height:10.5px}
.social{left:131px;top:1114px;width:94px;height:22px;border:1px solid var(--navy);border-radius:3px;display:flex;align-items:center;justify-content:space-evenly}
.social span{width:9px;height:9px;background:var(--navy);border-radius:2px}
.contact{left:348px;font-size:8px;line-height:10.5px;display:flex;gap:7px}
.offices{left:518px;top:1072px;font-size:9px;color:var(--orange-text)}
.office{top:1094px;font-size:7.8px;line-height:10.5px}
.office b{display:block;font-weight:400;color:var(--navy);margin-bottom:4px;font-size:8px}
.copy{left:0;top:1179px;width:900px;height:21px;background:#111;color:#fff;font-size:8px;text-align:center;line-height:21px}
</style>
</head>
<body>
<div class="page">
  <div class="abs topbar">
    <div class="abs mail"><svg width="10" height="7" viewBox="0 0 10 7"><rect x=".5" y=".5" width="9" height="6" fill="none" stroke="#fff"/><path d="M.5 .5 5 4 9.5 .5" fill="none" stroke="#fff"/></svg>hello@brightvoyage-intern.example</div>
    <div class="abs phone"><svg width="8" height="8" viewBox="0 0 8 8"><path d="M1 0h2l1 2-1 1c.5 1 1 1.5 2 2l1-1 2 1v2c-4 0-7-3-7-7z" fill="#fff"/></svg>+1 555 010 2480</div>
  </div>

  <header class="abs nav">
    <div class="abs brand"><span class="dot"></span>BRIGHT VOYAGE</div>
    <nav class="abs menu"><span>ABOUT US</span><span>DESTINATION</span><span>UNIVERSITIES</span><span>CONTACT</span></nav>
    <div class="abs search">Search<span class="btn"><svg width="8" height="8" viewBox="0 0 8 8"><circle cx="3.3" cy="3.3" r="2.5" fill="none" stroke="#222"/><path d="M5.2 5.2 7.5 7.5" stroke="#222"/></svg></span></div>
  </header>

  <section class="abs hero" role="img" aria-label="City skyline by the water at sunset"></section>
  <h1 class="abs" style="left:166px;top:126px;width:340px;font-family:'Merriweather',Georgia,serif;font-style:italic;font-weight:700;font-size:18px;line-height:22px;color:#fff">The Ideal intern is committed, creative, organized, and able to crack a smile</h1>

  <form class="abs form">
    <h2>Hospitality Internship<br>Registeration Form</h2>
    <div class="field" style="top:66px;height:32px">Name</div>
    <div class="field" style="top:106px;height:32px">Phone</div>
    <div class="field" style="top:145px;height:33px">Email</div>
    <div class="field" style="top:186px;height:55px">Massage</div>
    <div class="send">Sent</div>
  </form>

  <h3 class="abs title" style="top:396px">ABOUT US</h3>
  <p class="abs about-text">Having international experience and a global perspective in the field of education helps you become an educator that can serve all students. Education internships through Bright Voyage are less based in the classroom and more focused on education administration as a whole.</p>
  <div class="abs outline-btn">Read More</div>
  <div class="abs divider"></div>

  <h3 class="abs title" style="top:586px">DESTINATION</h3>
  <div class="abs tabs"><span class="on">Thailand</span><span>China</span><span>Spain</span><span>Brazil</span></div>
  <div class="abs dest photo" style="left:123px;background:linear-gradient(180deg,#2d4a7a,#6a5a4a)" role="img" aria-label="Temple by a river at dusk in Thailand"><span class="name">Thailand</span><span class="pill">More Info</span></div>
  <div class="abs dest photo" style="left:289px;background:linear-gradient(180deg,#4a74b8,#8a96a8)" role="img" aria-label="Modern glass building in China"></div>
  <div class="abs dest photo" style="left:455px;background:linear-gradient(180deg,#5a7ab0,#8a5a48)" role="img" aria-label="Historic town square in Spain"></div>
  <div class="abs dest photo" style="left:621px;background:linear-gradient(180deg,#7a90b8,#6a7a48)" role="img" aria-label="Pagodas on a green hillside"></div>

  <section class="abs unis" role="img" aria-label="Graduates throwing caps in the air"></section>
  <h3 class="abs title" style="top:834px;color:#fff">UNIVERSITIES</h3>
  <div class="abs uni photo" style="left:225px;background:linear-gradient(180deg,#2e4070,#4a5058)" role="img" aria-label="University campus building"><span class="name">Northfield<br>University</span></div>
  <div class="abs uni photo" style="left:382px;background:linear-gradient(180deg,#8a8f90,#5f8a48)" role="img" aria-label="Stone university hall with gardens"></div>
  <div class="abs uni photo" style="left:539px;background:linear-gradient(180deg,#8fb0d8,#b8a890)" role="img" aria-label="Modern campus building with trees"></div>
  <div class="abs white-btn">Show More</div>

  <p class="abs foot-about">International experience and a global perspective in the field of education helps you become an educator that can serve all students.</p>
  <div class="abs social" aria-label="Social links"><span></span><span></span><span></span><span></span><span></span></div>

  <div class="abs contact" style="top:1074px"><svg width="7" height="10" viewBox="0 0 7 10"><path d="M3.5 0A3.5 3.5 0 0 0 0 3.5C0 6 3.5 10 3.5 10S7 6 7 3.5A3.5 3.5 0 0 0 3.5 0z" fill="var(--navy)"/><circle cx="3.5" cy="3.5" r="1.2" fill="#fff"/></svg><span>27 Harbor Lane Marlow,<br>MD 20100</span></div>
  <div class="abs contact" style="top:1099px"><svg width="8" height="8" viewBox="0 0 8 8"><path d="M1 0h2l1 2-1 1c.5 1 1 1.5 2 2l1-1 2 1v2c-4 0-7-3-7-7z" fill="var(--navy)"/></svg><span>+1 555 010 2480</span></div>
  <div class="abs contact" style="top:1117px"><svg width="10" height="7" viewBox="0 0 10 7"><rect x=".5" y=".5" width="9" height="6" fill="none" stroke="var(--navy)"/><path d="M.5 .5 5 4 9.5 .5" fill="none" stroke="var(--navy)"/></svg><span>hello@brightvoyage-intern.example</span></div>

  <div class="abs offices">Our Main Offices</div>
  <div class="abs office" style="left:519px"><b>Thailand</b>8 Lotus Road Riverbend,<br>MD 20177</div>
  <div class="abs office" style="left:654px"><b>Chain</b>5 Jade Court Riverbend,<br>MD 20188</div>

  <footer class="abs copy">© copyright 2018 brightvoyage</footer>
</div>
</body>
</html>
```